Redesign of existing icons for mobile health app

I have approx 60 icons that i use in a mobile app (www.trailvistabuddy.com). These icons dont have the same look and feel and i am looking for someone that can "harmonize" these icons so that they all have the same style. I do not have a problem if you use an existing icon set as a basis but you will probably have to redesign some icons that are not available in the existing icon set.

Target Market(s)

Health & Fitness

Customers are mainly 40+ adults. The logo has to be clear and simple and self explanatory

Industry/Entity Type

Health

Requirements
Must have
• Clear and simple. All the same style

The logo is orange/blue. See attachment. Would be nice if you come up with a icon set that "fits" this logo.
Nice to have
• 3D effect would be nice

```html
<!DOCTYPE html>
<html lang="en">
<head>
<meta charset="utf-8">
<title>Trail Vista Buddy – status bar icons</title>
<link rel="stylesheet" href="https://fonts.googleapis.com/css2?family=Open+Sans:wght@400;600;700&display=swap">
<style>
  :root {
    --canvas: #d9dadc;
    --list-bg: #e6e8ea;
    --divider: #b9bcc0;
    --ink: #1b1b1b;
    --ink-soft: #3a3a3a;
    --bar-top: #33508f;
    --bar-mid: #4a69aa;
    --bar-low: #8ba6d9;
    --icon-line: #ffffff;
    --icon-shade: #4b4b4b;
    --thumb-light: #5d6066;
    --thumb-dark: #34363b;
  }
  * { margin: 0; padding: 0; box-sizing: border-box; }
  html, body { width: 1200px; height: 766px; overflow: hidden; }
  body {
    background: var(--canvas);
    font-family: "Open Sans", sans-serif;
    position: relative;
  }
  .screen {
    position: absolute;
    left: 0; top: 70px;
    width: 1200px; height: 626px;
    background: var(--list-bg);
    overflow: hidden;
  }
  .divider {
    position: absolute; left: 0; width: 100%; height: 4px;
    background: var(--divider);
  }
  .divider.top { top: 18px; }
  .divider.bottom { top: 303px; }
  .reading {
    position: absolute; left: 0; top: 22px; width: 100%; height: 281px;
  }
  .sensor-thumb {
    position: absolute; left: 48px; top: 66px;
    width: 160px; height: 200px;
    border-radius: 12px;
    background: linear-gradient(to bottom, var(--thumb-light) 0%, var(--thumb-dark) 100%);
  }
  .reading-value {
    position: absolute; left: 259px; top: 60px;
    font-size: 62px; font-weight: 700; color: var(--ink); line-height: 1;
  }
  .reading-time {
    position: absolute; left: 259px; top: 188px;
    font-size: 44px; font-weight: 600; color: var(--ink-soft); line-height: 1;
  }
  .reading-status {
    position: absolute; right: 27px; top: 72px;
    font-size: 48px; font-weight: 600; color: var(--ink-soft); line-height: 1;
  }
  .reading-note {
    position: absolute; right: 27px; top: 190px;
    font-size: 40px; font-weight: 600; color: var(--ink-soft); line-height: 1;
  }
  .status-bar {
    position: absolute; left: 0; top: 380px; width: 100%; height: 246px;
    background: linear-gradient(to bottom, var(--bar-top) 0%, var(--bar-mid) 35%, var(--bar-low) 78%, var(--bar-mid) 100%);
  }
  .info-icon { position: absolute; left: 38px; top: 10px; }
  .link-label {
    position: absolute; left: 790px; top: 78px;
    font-size: 34px; font-weight: 600; color: var(--icon-line); line-height: 1;
  }
  .battery-icon { position: absolute; left: 1000px; top: 22px; }
</style>
</head>
<body>
  <main class="screen">
    <div class="divider top"></div>
    <section class="reading">
      <div class="sensor-thumb" role="img" aria-label="Product photo of the heart-rate sensor"></div>
      <p class="reading-value">74 Pulse</p>
      <p class="reading-time">08-Feb (11:50)</p>
      <p class="reading-status">Normal</p>
      <p class="reading-note">None</p>
    </section>
    <div class="divider bottom"></div>

    <nav class="status-bar">
      <svg class="info-icon" width="190" height="220" viewBox="0 0 190 220" aria-label="Info">
        <circle cx="95" cy="96" r="88" fill="none" stroke="var(--icon-shade)" stroke-width="6"/>
        <circle cx="95" cy="96" r="82" fill="none" stroke="var(--icon-line)" stroke-width="6"/>
        <circle cx="95" cy="46" r="13" fill="var(--icon-line)" stroke="var(--icon-shade)" stroke-width="3"/>
        <path d="M72 72 H104 V150 H116 V164 H72 V150 H84 V86 H72 Z" fill="var(--icon-line)" stroke="var(--icon-shade)" stroke-width="3"/>
        <ellipse cx="95" cy="205" rx="85" ry="14" fill="none" stroke="var(--icon-line)" stroke-width="5" opacity="0.35"/>
      </svg>

      <span class="link-label">LinkWave</span>

      <svg class="battery-icon" width="130" height="210" viewBox="0 0 130 210" aria-label="Battery warning">
        <path d="M8 18 Q65 2 122 18 V158 Q65 174 8 158 Z" fill="rgba(255,255,255,0.12)" stroke="var(--icon-line)" stroke-width="5"/>
        <ellipse cx="65" cy="18" rx="57" ry="12" fill="none" stroke="var(--icon-line)" stroke-width="5"/>
        <ellipse cx="65" cy="16" rx="30" ry="5" fill="var(--icon-line)" opacity="0.7"/>
        <path d="M10 135 Q65 150 120 135 V158 Q65 174 10 158 Z" fill="var(--icon-line)" opacity="0.85"/>
        <rect x="59" y="48" width="12" height="58" fill="var(--icon-line)"/>
        <rect x="59" y="116" width="12" height="12" fill="var(--icon-line)"/>
        <path d="M10 172 Q65 186 120 172 V200 Q65 210 10 200 Z" fill="var(--icon-line)" opacity="0.25"/>
      </svg>
    </nav>
  </main>
</body>
</html>
```